Social house sales

An app that allows someone to search for houses for sale in a certain city or post code...then returns the results and allows the user to like or comment on each property for sale, and @mention others who are users.
UPDATE:
May i know whats your apps name?and please attach the logo.
also - No logo yet! But the name is ''Plimo''
can i get more specific how many pages you want? - Five pages of the mocked up is fine
can you provide the wireframe? - I haven''t done any wire frames, looking for inspiration! Registration/opening splash page, search page, results page, comment/liking, @mentioning someone - those could be five views
and are this app have profile page? No
login with qz or zelbo or pramvek? QZ
which OS i should design it? (IOS,Android) iOS
House buyers, renters
House

```html
<!DOCTYPE html>
<html lang="en">
<head>
<meta charset="utf-8">
<title>Property result</title>
<link rel="stylesheet" href="https://fonts.googleapis.com/css2?family=Lato:ital,wght@0,400;0,700;1,400&family=Open+Sans:wght@400;600;700&family=Roboto:wght@400;500&display=swap">
<style>
:root{
  --page-bg:#ececec;
  --screen-bg:#ffffff;
  --status-bg:#0d0d0d;
  --status-text:#ffffff;
  --brand:#8069c0;
  --brand-text:#ffffff;
  --title:#3a3a3a;
  --muted:#9a9a9a;
  --body:#222222;
  --line:#e3e3e3;
  --card-border:#d4d4d4;
  --card-foot:#f6f6f6;
  --tab-bg:#f8f8f8;
  --icon:#555555;
}
*{margin:0;padding:0;box-sizing:border-box}
html,body{width:683px;height:1200px;overflow:hidden;background:var(--page-bg)}
.screen{position:absolute;left:5px;top:0;width:673px;height:1200px;background:var(--screen-bg);overflow:hidden;font-family:'Lato',sans-serif}
.abs{position:absolute}

.status-bar{left:0;top:0;width:673px;height:49px;background:var(--status-bg);color:var(--status-text);font-family:'Roboto',sans-serif;font-weight:500}
.carrier{left:10px;top:10px;font-size:24px;display:flex;align-items:flex-end;gap:6px}
.signal{display:flex;align-items:flex-end;gap:2px;height:20px}
.signal i{display:block;width:4px;background:var(--status-text)}
.clock{left:0;width:673px;top:8px;text-align:center;font-size:27px}
.status-icons{right:12px;top:11px;display:flex;gap:12px;align-items:center}

.app-header{left:0;top:49px;width:673px;height:94px;background:var(--brand);border-bottom:4px solid #efeff4}
.back-button{left:34px;top:24px}
.app-title{left:0;width:673px;top:26px;text-align:center;color:var(--brand-text);font-family:'Roboto',sans-serif;font-size:31px;font-weight:400}

.property-photo{left:29px;top:175px;width:616px;height:422px;background:linear-gradient(135deg,#f6e6c4 0%,#e0a050 40%,#c97a2a 65%,#8a6046 100%)}
.property-name{left:29px;top:620px;font-size:23px;font-weight:700;color:var(--title)}
.property-price{right:28px;top:616px;font-size:31px;font-weight:700;color:var(--brand)}
.property-address{left:29px;top:655px;font-size:20px;font-style:italic;color:var(--muted)}
.property-stats{left:35px;top:700px;display:flex;font-size:20px;color:var(--title)}
.stat{display:flex;align-items:center;gap:12px;width:106px}
.section-divider{left:0;top:754px;width:673px;height:1px;background:var(--line)}

.comment-card{left:30px;top:787px;width:614px;height:260px;border:1px solid var(--card-border);background:var(--screen-bg);font-family:'Open Sans',sans-serif;overflow:hidden}
.avatar{left:19px;top:20px;width:52px;height:52px;background:linear-gradient(160deg,#d9d4cf,#6b5a52)}
.comment-meta{left:83px;top:14px;font-size:15px;color:var(--muted)}
.comment-meta b{color:var(--brand);font-weight:700}
.comment-body{left:83px;top:37px;width:515px;font-size:13.9px;line-height:21px;color:var(--body);letter-spacing:-0.1px}
.see-more{color:var(--brand);font-size:13px;margin-left:4px}
.comment-actions{left:83px;top:103px;font-size:15px;font-weight:700;color:var(--brand);display:flex;gap:30px}
.card-foot{left:0;top:143px;width:612px;height:115px;background:var(--card-foot);border-top:1px solid var(--card-border)}
.card-counts{left:23px;top:9px;display:flex;gap:18px;font-size:14.5px;font-weight:700;color:var(--body)}
.card-counts span{display:flex;align-items:center;gap:6px}
.card-rule{left:20px;top:43px;width:572px;height:1px;background:#d9d9d9}
.reply-field{left:24px;top:61px;width:566px;height:36px;background:#fff;border:1px solid #cfcfcf}

.tab-bar{left:0;top:1096px;width:673px;height:104px;background:var(--tab-bg);border-top:1px solid var(--line)}
.tab{top:25px;width:56px;height:56px;display:flex;align-items:center;justify-content:center}
</style>
</head>
<body>
<div class="screen">

  <div class="abs status-bar">
    <div class="abs carrier">
      <span class="signal"><i style="height:6px"></i><i style="height:9px"></i><i style="height:12px"></i><i style="height:15px"></i><i style="height:18px"></i></span>KG
    </div>
    <div class="abs clock">1:57 PM</div>
    <div class="abs status-icons">
      <svg width="22" height="22" viewBox="0 0 22 22"><circle cx="11" cy="11" r="10" fill="#fff"/><path d="M11 5v6h4" stroke="#0d0d0d" stroke-width="2" fill="none"/></svg>
      <svg width="22" height="22" viewBox="0 0 22 22"><path d="M21 1L1 10l9 2 2 9z" fill="#fff"/></svg>
      <svg width="26" height="26" viewBox="0 0 26 26"><path d="M22 13a9 9 0 1 1-3-6.7" stroke="#fff" stroke-width="2.4" fill="none"/><path d="M16 3l4 3.5-4.5 2z" fill="#fff"/><rect x="9" y="12" width="8" height="7" fill="#fff"/><path d="M10.5 12v-2a2.5 2.5 0 0 1 5 0v2" stroke="#fff" stroke-width="1.6" fill="none"/></svg>
      <svg width="38" height="20" viewBox="0 0 38 20"><rect x="1" y="2" width="32" height="16" rx="2" stroke="#fff" stroke-width="2" fill="none"/><rect x="4" y="5" width="26" height="10" fill="#fff"/><rect x="34" y="7" width="3" height="6" fill="#fff"/></svg>
    </div>
  </div>

  <header class="abs app-header">
    <svg class="abs back-button" width="44" height="44" viewBox="0 0 44 44" aria-label="Back"><circle cx="22" cy="22" r="20" stroke="#fff" stroke-width="2.4" fill="none"/><path d="M31 22H13M20 15l-7 7 7 7" stroke="#fff" stroke-width="2.4" fill="none" stroke-linecap="round" stroke-linejoin="round"/></svg>
    <h1 class="abs app-title">Result</h1>
  </header>

  <div class="abs property-photo" role="img" aria-label="Photo of the property: sunlit living room with wooden walls, sofa and armchairs"></div>

  <h2 class="abs property-name">The Name of The property</h2>
  <div class="abs property-price">$ 900,000</div>
  <p class="abs property-address">The address of the property</p>

  <div class="abs property-stats">
    <span class="stat"><svg width="24" height="22" viewBox="0 0 24 22"><path d="M2 9h4v12H2zM8 20V9l5-7c2 0 2.5 1.5 2 3l-1 4h6c1.5 0 2.5 1.2 2 2.6l-2.5 7.5c-.3 1-1.2 1.9-2.3 1.9z" stroke="#8069c0" stroke-width="1.8" fill="none" stroke-linejoin="round"/></svg>100</span>
    <span class="stat"><svg width="26" height="22" viewBox="0 0 26 22"><path d="M1 2h15v10H7l-4 4v-4H1z" fill="#8069c0"/><path d="M18 6h7v10h-2v4l-4-4h-8v-2h7z" fill="#8069c0"/></svg>20</span>
    <span class="stat"><svg width="24" height="20" viewBox="0 0 24 20"><path d="M14 1l9 8-9 8v-5C8 12 4 14 1 19c1-7 5-12 13-12z" fill="#8069c0"/></svg>15</span>
  </div>

  <div class="abs section-divider"></div>

  <article class="abs comment-card">
    <div class="abs avatar" role="img" aria-label="Commenter avatar"></div>
    <div class="abs comment-meta"><b>Derek</b> - 6 days ago</div>
    <p class="abs comment-body">Lorem ipsum dolor sit amet, consectetur adipiscing elit, sed do eiusmod<br>tempor incididunt ut labore et dolore magna aliqua. Ut enim minim veniam,<br>quis nostrud exercitation ullamco laboris nisi ut.<span class="see-more">see more</span></p>
    <div class="abs comment-actions"><span>like</span><span>comments</span></div>
    <div class="abs card-foot">
      <div class="abs card-counts">
        <span><svg width="16" height="15" viewBox="0 0 24 22"><path d="M2 9h4v12H2zM8 20V9l5-7c2 0 2.5 1.5 2 3l-1 4h6c1.5 0 2.5 1.2 2 2.6l-2.5 7.5c-.3 1-1.2 1.9-2.3 1.9z" stroke="#8069c0" stroke-width="2.2" fill="none"/></svg>30 like</span>
        <span><svg width="18" height="15" viewBox="0 0 26 22"><path d="M1 2h15v10H7l-4 4v-4H1z" fill="#8069c0"/><path d="M18 6h7v10h-2v4l-4-4h-8v-2h7z" fill="#8069c0"/></svg>2 comments</span>
      </div>
      <div class="abs card-rule"></div>
      <div class="abs reply-field"></div>
    </div>
  </article>

  <nav class="abs tab-bar">
    <span class="abs tab" style="left:37px"><svg width="52" height="52" viewBox="0 0 52 52"><circle cx="21" cy="21" r="15" stroke="#8069c0" stroke-width="2.6" fill="none"/><path d="M32 32l15 15" stroke="#8069c0" stroke-width="3" stroke-linecap="round"/></svg></span>
    <span class="abs tab" style="left:172px"><svg width="52" height="52" viewBox="0 0 52 52"><circle cx="26" cy="26" r="23" stroke="#555" stroke-width="2" fill="none"/><text x="26" y="34" text-anchor="middle" font-family="Lato,sans-serif" font-size="24" fill="#555">?</text></svg></span>
    <span class="abs tab" style="left:310px"><svg width="56" height="50" viewBox="0 0 56 50"><path d="M28 46C10 32 3 24 3 15A12 12 0 0 1 28 9a12 12 0 0 1 25 6c0 9-7 17-25 31z" stroke="#555" stroke-width="2" fill="none"/></svg></span>
    <span class="abs tab" style="left:448px"><svg width="56" height="52" viewBox="0 0 56 52"><path d="M30 14H4v34h38V34" stroke="#555" stroke-width="2" fill="none"/><path d="M10 40c2-12 12-20 26-20v8l14-13L36 3v8C20 12 12 24 10 40z" stroke="#555" stroke-width="2" fill="none" stroke-linejoin="round"/></svg></span>
    <span class="abs tab" style="left:586px"><svg width="54" height="46" viewBox="0 0 54 46"><path d="M27 3C14 3 3 10 3 20c0 5 3 9 7 12l-4 11 12-7c3 1 6 1 9 1 13 0 24-7 24-17S40 3 27 3z" stroke="#555" stroke-width="2" fill="none" stroke-linejoin="round"/></svg></span>
  </nav>

</div>
</body>
</html>
```